Flyer Design for sewing business

Hi. i need flyers for my new business called " Vora Stitchworks". I am based in Sauchie. I offer Door to Door Clothing Alteration Service!
I provide a door to door alteration service for Clackmannanshire area with 20 miles radiance! (I give free consultations at your preferred location where I can accurately quote the cost of the alteration, as this depends on the garment itself. I aim to deliver the completed item back to you within a week though often it is less than this.)
I also design and sew occasional girls dresses ( first communion, flower girl, party dresses)
The consultation are free with no commitment to take the service.

I wold like see designs that use colors similar to colors on my website, like dusty pink, orange.

To contact either phone MIRA 07912348806
or email: mira.tusk71@quellmail.com

www.brimlink.com/vorastitchworks
www.vora-stitchworks.pagenest.com

THAT IS THE Price List Jeans/Trousers: Shorten....................................from £10.00 Taken in (waist).......................from £8.00 Taken in (side seams)..............from £10.00 Replace zip...............................from £10.00 Dresses/Skirts: Shorten....................................from £10.00 Taken in (waist).......................from £8.00 Taken in (side seams)..............from £8.00 Replace zip...............................from £10.00 Jacket/Coat: Shorten sleeves........................from £12.00 Shorten length (Jacket)...........from £16.00 Shorten length (Coat)..............from £18.00 Taken in (back seam)...............from £12.00 Taken in (side seams)..............from £18.00 Repairs......................................from £5.00 Bridal: Shorten Wedding Dress...........from £25.00 All other bridal alteration quotes can be given on consultation.

Reason: HI, ALL! IN THE NEXT FEW DAYS I GONE EXPERIENCE HOUSE MOVE AND SOME STRESS INVOLVING IN THIS.THANK YOU ALL FOR UNDERSTANDING AND A PATIENCE!

```html
<!DOCTYPE html>
<html lang="en">
<head>
<meta charset="utf-8">
<title>Vora Stitchworks – Door to Door Alterations</title>
<link href="https://fonts.googleapis.com/css2?family=Cinzel:wght@400;700&family=Source+Sans+3:wght@400;600;700&display=swap" rel="stylesheet">
<style>
  :root{
    --paper:#ffffff;
    --rose:#d96f78;
    --rose-deep:#c85f69;
    --salmon:#f3946f;
    --ring:#ee8a5f;
    --ink:#3a3a3a;
    --brand:#3d3d3d;
    --white:#ffffff;
    --photo-a:#ece6e1;
    --photo-b:#e79aac;
    --photo-c:#f3d8c6;
  }
  *{box-sizing:border-box;margin:0;padding:0}
  html,body{width:927px;height:1200px;overflow:hidden;background:var(--paper)}
  .flyer{position:relative;width:927px;height:1200px;background:var(--paper);font-family:"Source Sans 3",Arial,sans-serif;color:var(--white)}
  .gallery{position:absolute;top:5px;left:0;width:927px;height:355px}
  .gallery .photo{position:absolute;top:0;height:355px}
  .photo-white-dress{left:5px;width:225px;background:linear-gradient(160deg,#f4f0ec,var(--photo-a) 60%,#d9cfc8)}
  .photo-pink-bow{left:235px;width:451px;background:radial-gradient(ellipse at 50% 35%,#f2b6c6,var(--photo-b) 55%,#c9788c)}
  .photo-peach-dress{left:692px;width:230px;background:linear-gradient(160deg,#efe3d6,var(--photo-c) 55%,#e2b49a)}
  .hero{position:absolute;top:360px;left:0;width:927px;height:292px;background:var(--rose)}
  .badge{position:absolute;left:364px;top:230px;width:200px;height:200px;border-radius:50%;background:var(--white);border:4px solid var(--ring);display:flex;align-items:center;justify-content:center;text-align:center}
  .badge-name{font-family:"Cinzel",Georgia,serif;font-weight:400;font-size:17px;color:var(--ink);letter-spacing:.5px;line-height:1.3}
  .title{position:absolute;top:110px;left:0;width:927px;text-align:center;font-family:"Cinzel",Georgia,serif;font-weight:400;font-size:62px;color:var(--brand);letter-spacing:1px}
  .tagline{position:absolute;top:212px;left:0;width:927px;text-align:center;font-size:15px;color:#fbe3e3}
  .details{position:absolute;top:655px;left:0;width:927px;height:479px;background:var(--salmon);border-top:1px solid #f7c3b3}
  .intro{position:absolute;top:22px;left:40px;width:847px;text-align:center;font-size:16px;line-height:22px}
  .promise{position:absolute;top:108px;left:0;width:927px;text-align:center;font-size:16px}
  .price-heading{position:absolute;top:158px;left:68px;font-family:"Cinzel",Georgia,serif;font-weight:700;font-size:28px;color:var(--ink)}
  .price-col{position:absolute;top:208px;list-style:none;font-size:15px;line-height:22px}
  .col-left{left:91px;width:330px}
  .col-right{left:480px;width:349px}
  .price-col li{display:flex;align-items:baseline}
  .price-col .item{white-space:nowrap}
  .price-col .dots{flex:1;border-bottom:1.5px dotted var(--white);margin:0 2px;transform:translateY(-4px)}
  .price-col .cost{white-space:nowrap}
  .price-col .head{font-weight:700}
  .price-col .gap{margin-top:17px}
  .bridal-note{position:absolute;top:345px;left:480px;width:320px;font-size:15px;line-height:22px}
  .contact-bar{position:absolute;top:1134px;left:0;width:927px;height:66px;background:var(--rose);border-top:1px solid #f4c0b8;color:var(--ink);font-weight:700;font-size:15px}
  .contact-phone{position:absolute;left:33px;top:24px}
  .contact-email{position:absolute;left:326px;top:24px}
  .contact-web{position:absolute;left:632px;top:13px;line-height:19px}
</style>
</head>
<body>
<main class="flyer">
  <section class="gallery">
    <div class="photo photo-white-dress" role="img" aria-label="Photo of a white satin girls dress with pink rose sash"></div>
    <div class="photo photo-pink-bow" role="img" aria-label="Close-up photo of a pink satin bow with a sparkling buckle"></div>
    <div class="photo photo-peach-dress" role="img" aria-label="Photo of a peach tulle party dress with cream flower trim"></div>
  </section>

  <section class="hero">
    <h1 class="title">VORA STITCHWORKS</h1>
    <p class="tagline">Door to door alteration service for Clackmannanshire area (within 20 miles radiance)</p>
  </section>

  <div class="badge"><span class="badge-name">VORA<br>STITCHWORKS</span></div>

  <section class="details">
    <p class="intro">I provide a free consultations at your preferred location where I can accurately quote the cost of the alteration, as this depends on the garment itself. I aim to deliver the completed item back to you within a week or less!<br>I also design and sew occasional girls dresses (First Communion, flower girl, party dresses)</p>
    <p class="promise">The consultation is FREE with no commitment to take the service.</p>

    <h2 class="price-heading">Price List:</h2>

    <ul class="price-col col-left">
      <li><span class="item head">Jeans/Trousers Shorten</span><span class="dots"></span><span class="cost">from £10.00</span></li>
      <li><span class="item">Taken In Waist</span><span class="dots"></span><span class="cost">from £8.00</span></li>
      <li><span class="item">Taken In Side Seams</span><span class="dots"></span><span class="cost">from £10.00</span></li>
      <li><span class="item">Replace Zip</span><span class="dots"></span><span class="cost">from £10.00</span></li>
      <li class="gap"><span class="item head">Jacket/Coat Shorten Sleeves</span><span class="dots"></span><span class="cost">from £12.00</span></li>
      <li><span class="item">Shorten Length (Jacket)</span><span class="dots"></span><span class="cost">from £16.00</span></li>
      <li><span class="item">Shorten Length (Coat)</span><span class="dots"></span><span class="cost">from £18.00</span></li>
      <li><span class="item">Taken In (Back Seam)</span><span class="dots"></span><span class="cost">from £12.00</span></li>
      <li><span class="item">Taken In (Side Seams)</span><span class="dots"></span><span class="cost">from £18.00</span></li>
      <li><span class="item">Repairs</span><span class="dots"></span><span class="cost">from £5.00</span></li>
    </ul>

    <ul class="price-col col-right">
      <li><span class="item head">Dresses/Skirts Shorten</span><span class="dots"></span><span class="cost">from £10.00</span></li>
      <li><span class="item">Taken In Waist</span><span class="dots"></span><span class="cost">from £8.00</span></li>
      <li><span class="item">Taken In Side Seams</span><span class="dots"></span><span class="cost">from £10.00</span></li>
      <li><span class="item">Replace Zip</span><span class="dots"></span><span class="cost">from £10.00</span></li>
      <li class="gap"><span class="item head">Bridal: Shorten Wedding Dress</span><span class="dots"></span><span class="cost">from £25.00</span></li>
    </ul>

    <p class="bridal-note">All other bridal alteration quotes can be given on consultation.</p>
  </section>

  <footer class="contact-bar">
    <span class="contact-phone">Phone: MIRA 07912348806</span>
    <span class="contact-email">Email: mira.tusk71@quellmail.com</span>
    <span class="contact-web">www.vora-stitchworks.pagenest.com<br>www.brimlink.com/vorastitchworks</span>
  </footer>
</main>
</body>
</html>
```